e-Book Cover Design Project

I need an e-book cover design for a book called The Quiet Orchard. A handbook for hearts (turned sour). It is non-fiction. It has an apple theme throughout so I would like to see designs that use a red apple (perhaps even a bite out of it), simple text and simple background. Despite the theme, the final design should still be positive.

Target Market(s)

Most likely women aged 25 and over.

Requirements
Must have
• real red apple
Nice to have
• cupids arrow
Should not have
• cartoons

```html
<!DOCTYPE html>
<html lang="en">
<head>
<meta charset="utf-8">
<title>The Quiet Orchard — Cover</title>
<link rel="stylesheet" href="https://fonts.googleapis.com/css2?family=EB+Garamond:ital,wght@0,400;1,400&family=Playfair+Display:ital,wght@1,400&display=swap">
<style>
  :root {
    --leaf-green: #7f9a55;
    --meadow: #b7c48a;
    --fruit-orange: #e98a22;
    --fruit-amber: #f2b13a;
    --apple-red: #d8472a;
    --halo: rgba(255, 214, 150, 0.32);
    --title-white: #ffffff;
    --title-edge: rgba(120, 55, 15, 0.55);
    --ink: #141210;
  }
  html, body {
    margin: 0;
    padding: 0;
    width: 776px;
    height: 1200px;
    overflow: hidden;
    background: #ffffff;
  }
  .cover {
    position: relative;
    width: 776px;
    height: 1200px;
    overflow: hidden;
  }
  .cover-photo {
    position: absolute;
    inset: 0;
    background:
      radial-gradient(circle at 550px 900px, var(--apple-red) 0, #c8422a 150px, rgba(200, 66, 42, 0) 200px),
      radial-gradient(ellipse at 300px 300px, var(--fruit-amber) 0, var(--fruit-orange) 260px, rgba(233, 138, 34, 0) 520px),
      linear-gradient(180deg, #c9781f 0%, #b07a2e 45%, var(--leaf-green) 68%, var(--meadow) 100%);
  }
  .title-halo {
    position: absolute;
    inset: 0;
  }
  .title {
    position: absolute;
    top: 0;
    left: 0;
    margin: 0;
    font-family: "Playfair Display", Georgia, serif;
    font-style: italic;
    font-weight: 400;
    color: var(--title-white);
    text-shadow: 3px 3px 0 var(--title-edge);
    line-height: 1;
  }
  .title-line {
    position: absolute;
    white-space: nowrap;
  }
  .title-the { left: 318px; top: 40px; font-size: 215px; }
  .title-quiet { left: 96px; top: 228px; font-size: 175px; }
  .title-orchard { left: 60px; top: 400px; font-size: 160px; }
  .subtitle {
    position: absolute;
    left: 462px;
    top: 770px;
    margin: 0;
    font-family: "EB Garamond", Georgia, serif;
    font-style: italic;
    font-size: 42px;
    line-height: 51px;
    color: var(--title-white);
  }
  .subtitle span { display: block; }
  .subtitle .sub-a { padding-left: 100px; }
  .subtitle .sub-for { padding-left: 6px; }
  .subtitle .sub-turned { padding-left: 12px; }
  .author {
    position: absolute;
    left: 44px;
    top: 880px;
    margin: 0;
    font-family: "EB Garamond", Georgia, serif;
    font-weight: 400;
    font-size: 54px;
    line-height: 64px;
    color: var(--ink);
  }
  .author span { display: block; }
</style>
</head>
<body>
  <main class="cover">
    <div class="cover-photo" role="img" aria-label="Photograph of ripe orange and red apples hanging on a branch with green leaves, against a soft blurred meadow"></div>
    <svg class="title-halo" width="776" height="1200" viewBox="0 0 776 1200" aria-hidden="true">
      <circle cx="359" cy="300" r="372" fill="var(--halo)"/>
    </svg>
    <h1 class="title">
      <span class="title-line title-the">The</span>
      <span class="title-line title-quiet">Quiet</span>
      <span class="title-line title-orchard">Orchard</span>
    </h1>
    <p class="subtitle">
      <span class="sub-a">A</span>
      <span class="sub-handbook">handbook</span>
      <span class="sub-for">for hearts</span>
      <span class="sub-turned">(turned sour)</span>
    </p>
    <p class="author">
      <span>Clara</span>
      <span>Whitfield</span>
    </p>
  </main>
</body>
</html>
```